Webdesign für eine Softwarewarentwicklung und Consulting für das Gesundheitswesen
Zielgruppe
Softwarewarentwicklung und Consulting für das Gesundheitswesen. Unsere Zielgruppe sind Unternehmen und Organisationen im Bereich des Gesundheitswesen. Weiter informationen auf derzeitiger Homepage unter www.rulpo-medtechnik.de.
Aufgabenstellung
Das Webdesign sollte deutlich moderner und kreativer wirken als unsere derzeitige Hompage. (Die bisherige Hompage wurde seinerzeit bei der Gründung 'auf die Schnelle' entwickelt.) Die neue Homapage sollte 'frisch' wirken und einem modernen Softwareunternehmen entsprechen.: Schlicht, modern und innovativ. Die Website sollte auch später gut auf Handy und Tablet darstellbar sein. Da wir derzeit wenig Inhalte auf unserer Homepage haben, wären wir auch für inhaltliche Vorschläge dankbar. Unsere Logofarben sollten sich auch im Design wiederfinden (der Rotton hat den Wert RGB: 227, 7, 19 #e30713 - der Blauton hat den Wert RGB: 30, 38, 74 1 #e264a).
Im Format bin ich unerfahren und würde dann für das spätere Umsetzen Adobe Photoshop vorschlagen.
Idealerweise sollte sich das Design später in einem gängigen CMS umsetzen lassen.
Gerne können Sie uns auch ein Komplettangebot auch zum Thema Umsetzung unterbreiten.
Grundsätzlich finde ich folgende Hompages ganz gut:
https://fernlix.com/
https://www.brimvolk.de/
https://www.quenmarstudio.com/de/
https://vek-lum.de/

```html
<!DOCTYPE html>
<html lang="de">
<head>
<meta charset="utf-8">
<title>RULPO – Softwareentwicklung für das Gesundheitswesen</title>
<link href="https://fonts.googleapis.com/css2?family=Inter+Tight:wght@400;500;600;700&display=swap" rel="stylesheet">
<style>
:root{
  --red:#e30713;
  --navy:#1e264a;
  --ink:#1e264a;
  --text:#4a4f63;
  --line:#b9bcc6;
  --light:#efefef;
  --white:#ffffff;
}
*{margin:0;padding:0;box-sizing:border-box}
html,body{width:1200px;height:4408px;overflow:hidden;background:var(--white)}
body{position:relative;font-family:"Inter Tight",Arial,sans-serif;color:var(--ink);letter-spacing:-0.01em}
.abs{position:absolute}
.accent{color:var(--red)}

/* Header */
.brand{left:89px;top:20px;font-size:34px;font-weight:700;color:var(--red);letter-spacing:-0.02em;line-height:1}
.nav{left:678px;top:30px;display:flex;gap:20px;font-size:12px;color:var(--ink)}
.cta{left:955px;top:19px;width:161px;height:37px;border:2px solid var(--red);color:var(--ink);font-size:11px;display:flex;align-items:center;justify-content:center}

/* Hero */
.hero-title{left:176px;top:208px;font-size:38px;font-weight:700;line-height:1.08;letter-spacing:-0.03em}
.hero-text{left:176px;top:322px;width:520px;font-size:14px;line-height:1.35;color:var(--text)}
.hero-visual{left:0;top:515px;width:1200px;height:437px;background:linear-gradient(100deg,#c9b9a6 0%,#e9e1d6 35%,#8e8f92 55%,#e6e3df 75%,#9fb3c7 100%)}

/* Services */
.section-title{font-size:28px;font-weight:700;line-height:1.22;letter-spacing:-0.025em}
.services-title{left:176px;top:1083px}
.services-text{left:176px;top:1180px;width:320px;font-size:10.5px;line-height:1.5;color:var(--text)}
.services-text p+p{margin-top:12px}
.service-list{left:697px;top:1062px;width:414px;list-style:none}
.service-list li{height:67px;border-bottom:2px solid var(--line);display:flex;align-items:center;position:relative}
.service-list li:last-child{border-bottom:none}
.service-num{font-size:13px;width:30px;color:var(--ink)}
.service-name{font-size:21px;font-weight:700;letter-spacing:-0.02em}
.service-plus{position:absolute;right:8px;top:22px;width:24px;height:24px}

/* Statement */
.team-visual-a{left:89px;top:1578px;width:510px;height:499px;background:linear-gradient(135deg,#d7d3cc,#9aa6b7 60%,#5b79a4)}
.statement{left:599px;top:1640px;width:601px;height:437px;background:var(--navy)}
.statement-text{left:697px;top:1706px;width:400px;font-size:27px;font-weight:700;line-height:1.55;color:var(--white);letter-spacing:-0.03em}
.talk{left:599px;top:1953px;width:250px;height:248px;background:var(--red);color:var(--white)}
.talk-text{position:absolute;left:19px;top:20px;font-size:22px;line-height:1.15;letter-spacing:-0.02em}
.talk svg{position:absolute;left:19px;top:195px}

/* Approach */
.approach-title{left:99px;top:2304px}
.approach-text{left:99px;top:2402px;width:320px;font-size:10.5px;line-height:1.5;color:var(--text)}
.feature{width:320px;top:2505px}
.feature svg{position:absolute;left:0;top:0}
.feature-title{position:absolute;left:81px;top:4px;font-size:16px;font-weight:700;line-height:1.25;letter-spacing:-0.02em}
.feature-rule{position:absolute;left:81px;top:63px;width:185px;height:3px;background:var(--red)}
.feature-text{position:absolute;left:81px;top:82px;width:215px;font-size:10px;line-height:1.5;color:var(--text)}

/* Quote */
.quote-band{left:0;top:2802px;width:1200px;height:375px;background:var(--light)}
.portrait{left:193px;top:2868px;width:312px;height:309px;background:linear-gradient(180deg,#d9d4cf 0%,#c7b8ad 35%,#2b3758 60%,#243052 100%);border-radius:150px 150px 0 0}
.quote{left:609px;top:2916px;width:460px;font-size:20px;line-height:1.3;color:var(--ink);letter-spacing:-0.02em}
.quote-name{left:609px;top:3028px;font-size:13px;font-weight:600}
.quote-role{left:609px;top:3050px;font-size:10px;color:#7a7f8f}

/* Team */
.team-title{left:89px;top:3354px;width:530px}
.team-text{left:697px;top:3350px;width:330px;font-size:10.5px;line-height:1.5;color:var(--text)}
.photo-c{left:644px;top:3600px;width:457px;height:314px;background:linear-gradient(135deg,#d8dde0,#a9b3b5 55%,#6e7f86)}
.photo-a{left:89px;top:3540px;width:327px;height:368px;background:linear-gradient(160deg,#e7e5e2,#b7aea4 55%,#4a4b52)}
.photo-b{left:371px;top:3715px;width:348px;height:252px;background:linear-gradient(120deg,#1f3140,#3f6a86 50%,#c7a07b 80%,#26343f)}

/* Footer */
.site-footer{left:0;top:4092px;width:1200px;height:316px;background:var(--navy)}
.footer-brand{left:89px;top:4132px;font-size:34px;font-weight:700;color:var(--white);letter-spacing:-0.02em;line-height:1}
.f-head{font-size:14px;font-weight:600;top:4138px;color:var(--white)}
.f-list{list-style:none;font-size:10px;top:4180px;color:var(--white)}
.f-list li{height:23px;display:flex;align-items:center;white-space:nowrap}
.f-dash li::before{content:"";width:18px;height:1px;background:var(--red);margin-right:8px}
.contact li{height:31px;display:flex;align-items:flex-start;gap:12px}
.contact svg{flex:none}
.f-bottom{top:4375px;font-size:8.5px;color:var(--white);white-space:nowrap}
.f-dot{display:inline-block;width:8px;height:8px;border-radius:50%;border:1px solid var(--red);margin-right:8px;vertical-align:-1px}
</style>
</head>
<body>

<!-- Header -->
<div class="abs brand">RULPO</div>
<nav class="abs nav"><span>Home</span><span>Produkte</span><span>Über Uns</span><span>Jobangebote</span></nav>
<div class="abs cta">Beratung vereinbaren</div>

<!-- Hero -->
<h1 class="abs hero-title">Wir entwickeln digitale <span class="accent">Anwendungen</span><br>für die Zukunft im Gesundheitswesen</h1>
<p class="abs hero-text">Lorem ipsum dolor sit amet, consetetur sadipscing elitr, sed diam nonumy eirmod tempor invidunt ut labore et dolore magna aliquyam erat, sed diam voluptua. At vero eos et accusam et justo duo dolores et ea rebum. Stet clita kasd gubergren,</p>
<div class="abs hero-visual" role="img" aria-label="Foto: Team bespricht Ergebnisse am Laptop"></div>

<!-- Services -->
<h2 class="abs section-title services-title">Herausragende<br><span class="accent">Serviceleistungen</span></h2>
<div class="abs services-text">
  <p>Lorem ipsum dolor sit amet, consetetur sadipscing elitr, sed diam nonumy eirmod tempor invidunt ut labore et dolore magna aliquyam erat, sed diam voluptua. At vero eos et accusam et justo</p>
  <p>duo dolores et ea rebum. Stet clita kasd gubergren, no sea takimata sanctus est Lorem ipsum dolor sit amet. Lorem ipsum dolor sit amet, consetetur sadipscing elitr, sed diam nonumy</p>
</div>
<ul class="abs service-list">
  <li><span class="service-num">01</span><span class="service-name">Prozessoptimierung</span><svg class="service-plus" viewBox="0 0 24 24"><path d="M12 0v24M0 12h24" stroke="#e30713" stroke-width="2"/></svg></li>
  <li><span class="service-num">02</span><span class="service-name">Digitalisierung</span><svg class="service-plus" viewBox="0 0 24 24"><path d="M12 0v24M0 12h24" stroke="#e30713" stroke-width="2"/></svg></li>
  <li><span class="service-num">03</span><span class="service-name">Onlineanwendung</span><svg class="service-plus" viewBox="0 0 24 24"><path d="M12 0v24M0 12h24" stroke="#e30713" stroke-width="2"/></svg></li>
  <li><span class="service-num">04</span><span class="service-name">eRezept / E-Health</span><svg class="service-plus" viewBox="0 0 24 24"><path d="M12 0v24M0 12h24" stroke="#e30713" stroke-width="2"/></svg></li>
  <li><span class="service-num">05</span><span class="service-name">Consulting</span><svg class="service-plus" viewBox="0 0 24 24"><path d="M12 0v24M0 12h24" stroke="#e30713" stroke-width="2"/></svg></li>
  <li><span class="service-num">06</span><span class="service-name">Projektmanagement</span><svg class="service-plus" viewBox="0 0 24 24"><path d="M12 0v24M0 12h24" stroke="#e30713" stroke-width="2"/></svg></li>
</ul>

<!-- Statement -->
<div class="abs team-visual-a" role="img" aria-label="Foto: zwei Kollegen arbeiten gemeinsam am Laptop"></div>
<div class="abs statement"></div>
<p class="abs statement-text">Wir digitalisieren das Gesundheitswesen mit innovativen Services und verlässlichem Know-How.</p>
<div class="abs talk">
  <div class="talk-text">Besprechen wir<br>Ihre Ziele</div>
  <svg width="58" height="24" viewBox="0 0 58 24"><path d="M0 12h55M45 2l10 10-10 10" fill="none" stroke="#fff" stroke-width="2.5"/></svg>
</div>

<!-- Approach -->
<h2 class="abs section-title approach-title">Wir finden den<br><span class="accent">passenden</span> Ansatz</h2>
<p class="abs approach-text">Lorem ipsum dolor sit amet, consetetur sadipscing elitr, sed diam nonumy eirmod tempor invidunt ut labore et dolore magna aliquyam erat, sed diam voluptua. At vero eos et accusam et justo</p>

<div class="abs feature" style="left:99px">
  <svg width="54" height="56" viewBox="0 0 54 56" fill="none" stroke="#1e264a" stroke-width="1.5"><path d="M19 2h16v17h17v17H35v18H19V36H2V19h17z"/><circle cx="27" cy="27" r="3"/><path d="M10 27h14M30 27h14M27 10v14M27 30v14"/></svg>
  <div class="feature-title">Erfahrung im<br>Gesundheitswesen</div>
  <div class="feature-rule"></div>
  <div class="feature-text">Lorem ipsum dolor sit amet, consetetur sadipscing elitr, sed diam nonumy eirmod tempor invidunt ut labore et dolore magna</div>
</div>
<div class="abs feature" style="left:445px">
  <svg width="54" height="56" viewBox="0 0 54 56" fill="none" stroke="#1e264a" stroke-width="1.5"><path d="M30 54V44h8l2-8 5-2-4-8c0-13-10-22-22-22S3 13 3 25c0 8 4 13 9 17v12"/><circle cx="20" cy="23" r="9"/><circle cx="20" cy="23" r="3"/><path d="M20 10v4M20 32v4M7 23h4M29 23h4M11 14l3 3M26 29l3 3M29 14l-3 3M14 29l-3 3"/></svg>
  <div class="feature-title">Starke Fachkompetenz &amp;<br>IT-Know-How</div>
  <div class="feature-rule"></div>
  <div class="feature-text">Lorem ipsum dolor sit amet, consetetur sadipscing elitr, sed diam nonumy eirmod tempor invidunt ut labore et dolore magna</div>
</div>
<div class="abs feature" style="left:793px">
  <svg width="54" height="56" viewBox="0 0 54 56" fill="none" stroke="#1e264a" stroke-width="1.5"><circle cx="27" cy="27" r="25"/><path d="M14 50V26h10v24M24 50V14h10v36M34 50V30h8v16M29 14V7M17 31h4M17 37h4M17 43h4M27 20h4M27 26h4M27 32h4M27 38h4"/></svg>
  <div class="feature-title">Innovative Lösungen &amp;<br>schlanke Prozesse</div>
  <div class="feature-rule"></div>
  <div class="feature-text">Lorem ipsum dolor sit amet, consetetur sadipscing elitr, sed diam nonumy eirmod tempor invidunt ut labore et dolore magna</div>
</div>

<!-- Quote -->
<div class="abs quote-band"></div>
<div class="abs portrait" role="img" aria-label="Porträt des Geschäftsführers im Anzug"></div>
<p class="abs quote">"Wir helfen Unternehmen im Gesundheitswesen den digitalen Wandel zu gestalten und sich schlagkräftig zu positionieren."</p>
<div class="abs quote-name">Jonas Weberling</div>
<div class="abs quote-role">Geschäftsführer RULPO</div>

<!-- Team -->
<h2 class="abs section-title team-title">Ein Team. Viele Möglichkeiten. RULPO bietet <span class="accent">talentierten Menschen</span> Karriere-Chancen und Work-Life-Balance.</h2>
<p class="abs team-text">Lorem ipsum dolor sit amet, consetetur sadipscing elitr, sed diam nonumy eirmod tempor invidunt ut labore et dolore magna aliquyam erat, sed diam voluptua. At vero eos et accusam et justo</p>
<div class="abs photo-c" role="img" aria-label="Foto: Kollegen im hellen Großraumbüro"></div>
<div class="abs photo-a" role="img" aria-label="Foto: Mitarbeiterin und Mitarbeiter mit Laptop"></div>
<div class="abs photo-b" role="img" aria-label="Foto: Team hinter einer Glaswand mit Diagrammen"></div>

<!-- Footer -->
<footer class="abs site-footer"></footer>
<div class="abs footer-brand">RULPO</div>

<div class="abs f-head" style="left:291px">Kontakt</div>
<ul class="abs f-list contact" style="left:291px">
  <li><svg width="16" height="16" viewBox="0 0 24 24"><path d="M6 2l4 5-2 3c1 3 3 5 6 6l3-2 5 4-2 4C11 22 2 13 2 4z" fill="#e30713"/></svg><span>+49 30 12 / 4 56 70 - 00</span></li>
  <li><svg width="16" height="14" viewBox="0 0 24 18"><rect x="0" y="0" width="24" height="18" rx="2" fill="#e30713"/><path d="M1 2l11 8 11-8" stroke="#1e264a" stroke-width="1.6" fill="none"/></svg><span>info@rulpo-medtechnik.de</span></li>
  <li><svg width="16" height="16" viewBox="0 0 24 24" fill="none" stroke="#e30713" stroke-width="1.8"><circle cx="12" cy="12" r="10"/><path d="M2 12h20M12 2c4 4 4 16 0 20M12 2c-4 4-4 16 0 20"/></svg><span>rulpo-medtechnik.de</span></li>
  <li style="height:auto"><svg width="16" height="16" viewBox="0 0 24 24"><path d="M12 1a8 8 0 0 0-8 8c0 6 8 14 8 14s8-8 8-14a8 8 0 0 0-8-8z" fill="#e30713"/><circle cx="12" cy="9" r="3" fill="#1e264a"/></svg><span style="line-height:1.9">RULPO AG<br>Birkenweg 12<br>10115 Berlin</span></li>
</ul>

<div class="abs f-head" style="left:663px">Leistungen</div>
<ul class="abs f-list f-dash" style="left:663px">
  <li>Prozessoptimierung</li><li>Digitalisierung</li><li>Onlineanwendung</li><li>eRezept / E-Health</li><li>Consulting</li><li>Projektmanagement</li>
</ul>

<div class="abs f-head" style="left:870px">Unternehmen</div>
<ul class="abs f-list f-dash" style="left:870px">
  <li>Produkte</li><li>Über Uns</li><li>Jobangebote</li><li>Kontakt</li>
</ul>

<div class="abs f-bottom" style="left:89px"><span class="f-dot"></span>RULPO - Softwareentwicklung für das Gesundheitswesen</div>
<div class="abs f-bottom" style="left:472px">Impressum</div>
<div class="abs f-bottom" style="left:536px">Datenschutz</div>
<div class="abs f-bottom" style="left:604px">Cookie-Einstellungen</div>

</body>
</html>
```